Book Cover Design Project

Hello,

I am looking to get a cover created for my book.

Size 6 X 9

Title:
Quiet Ledger Steady Gains

Sub-Title:
Plain Methods for Growing Steady Gains Within Your Quiet Ledger

Author:
Martin Fenwick

The book could have an image or only typography.

If it does include an image do not use an image of a real person. If you use a person, he can be shaded in, outlined, etc

I like the color white and blue however, I am open to other colors as well.

Below is the cover of my previous book that has an image:
http://www.quillmarket.example/Dawn-Of-Stag-Path-Vowed-Final/dp/284610375K/ref=sr_1_1?ie=UTF8&s=books&qid=2417307529&sr=1-1

I like simple designs but open to other concepts also

attached is the text to be used for the back of the book.

Thank you in advance for your designs,

Target Market(s)

This book will be for small business owners. Typically males/females between the age of 25 - 45 looking to make more money without going broke with marketing.

Industry/Entity Type

Business

Requirements
Must have
• Must include the Title, Subtitle and Author on the cover

Nice to have
• An image that represents a small business growing
Should not have
• Images of a real person. Stylized versions are ok.

```html
<!DOCTYPE html>
<html lang="en">
<head>
<meta charset="utf-8">
<title>Quiet Ledger Steady Gains — Cover</title>
<link rel="stylesheet" href="https://fonts.googleapis.com/css2?family=Encode+Sans+Condensed:wght@400;500&family=Anton&display=swap">
<style>
  :root {
    --stage: #d4d4d6;
    --band-blue: #1a3fa8;
    --band-indigo: #1a1aa0;
    --band-violet: #6a4e9c;
    --ribbon: #c6d4f4;
    --body-top: #c3cdee;
    --body-bottom: #cad8ff;
    --ink-title: #2437b0;
    --ink-dark: #14155a;
    --sun-yellow: #f2e21c;
    --sun-orange: #f57a14;
    --sun-deep: #f06a10;
  }
  * { margin: 0; padding: 0; box-sizing: border-box; }
  html, body { width: 982px; height: 1200px; overflow: hidden; }
  body {
    background: var(--stage);
    display: flex;
    align-items: center;
    justify-content: center;
  }
  .cover {
    position: relative;
    width: 760px;
    height: 1140px;
    overflow: hidden;
    background: linear-gradient(180deg, var(--body-top), var(--body-bottom));
    box-shadow: 0 10px 30px rgba(0,0,0,0.25);
  }
  .top-band {
    position: absolute; left: 0; top: 0; width: 100%; height: 110px;
    background: linear-gradient(90deg, var(--band-blue) 0%, var(--band-indigo) 45%, var(--band-violet) 100%);
  }
  .top-band-shade {
    position: absolute; left: 0; top: 110px; width: 100%; height: 50px;
    background: linear-gradient(180deg, #8e95a8 0%, #b4bed6 100%);
  }
  .title-ribbon {
    position: absolute; left: 0; top: 160px; width: 100%; height: 180px;
    background: var(--ribbon);
    box-shadow: 0 8px 14px rgba(70,80,120,0.35);
    display: flex; align-items: center; justify-content: center;
  }
  .title {
    font-family: "Encode Sans Condensed", sans-serif;
    font-weight: 500;
    font-size: 66px;
    letter-spacing: -2px;
    color: var(--ink-title);
    white-space: nowrap;
    text-shadow: 0 0 6px #fff, 0 0 12px #fff, 2px 2px 0 #0d1670;
  }
  .title .title-big { font-size: 84px; }
  .subtitle {
    position: absolute; left: 60px; right: 60px; top: 450px;
    font-family: "Encode Sans Condensed", sans-serif;
    font-weight: 400;
    font-size: 34px;
    line-height: 1.25;
    letter-spacing: -1px;
    text-align: center;
    color: var(--ink-dark);
    text-shadow: 1px 1px 0 #fff;
  }
  .author-band {
    position: absolute; left: 0; bottom: 0; width: 100%; height: 270px;
    background: radial-gradient(ellipse 260px 180px at 38% 62%, var(--sun-yellow) 0%, #f5b21a 45%, transparent 80%),
                linear-gradient(90deg, var(--sun-orange) 0%, var(--sun-deep) 100%);
    box-shadow: 0 -10px 16px rgba(80,90,130,0.35);
  }
  .author {
    position: absolute; right: 90px; top: 98px;
    font-family: "Anton", sans-serif;
    font-size: 52px;
    letter-spacing: 1px;
    text-transform: uppercase;
    color: var(--ink-dark);
    text-shadow: 0 0 4px rgba(255,255,200,0.6);
  }
</style>
</head>
<body>
  <main class="cover">
    <div class="top-band"></div>
    <div class="top-band-shade"></div>
    <header class="title-ribbon">
      <h1 class="title">Quiet Ledger <span class="title-big">Steady Gains</span></h1>
    </header>
    <p class="subtitle">Plain Methods for Growing Steady Gains<br>Within Your Quiet Ledger</p>
    <footer class="author-band">
      <p class="author">Martin Fenwick</p>
    </footer>
  </main>
</body>
</html>
```